Professional Website Design to match new logo for Medical Legal Company

We have rebranded our company and We want a professional but also dynamic web site design for a group of esteemed doctors that provide expert evaluation of an injured worker in a Workers Compensation case.
​
1. Our target market is both the attorneys who select our doctors and any doctors who would wish to join our group.

2. Notes for the Landing Page:
- We prefer a simpler, sleeker more modern look for the landing page.
- We want a simplified landing page with one image, three buttons highlighted in Content document.
- We want the main image to be black and white but it can be splashed with color.
-We think the landing page might be enhanced by add a dark blue or black as a primary color. Of course please feel free to try any color combination you think might work.
- We want "The Meridale Circle" in large letters and "Stewards of a fair and prompt outcome" in small lettering. We don't want icons on the buttons.
- Do not want more than the one picture at top of landing page.
- We do not want any pictures that include faces. Please eliminate or replace. They will not be chosen.
- For the landing page, instead of a second set of photos please experiment with using medical symbols and legal symbols.
​
3. New Company Name: The Meridale Circle
New logo is uploaded bronze and grey/silver will be colors although we are still tweaking the colors for more metallic feel. Want simple not busy.

4. The overall Web page design needs to have some website design effect (e,g image rollover, scrolling effect, hover effect etc).

5. Please follow the attached word document file for the page content of the 4 web pages. Do not mix it up.

Previous company website: www.clinicjuristpanel.example (we wish to convert some of the content from this website to the new brand). Competitor website that we like: www.docboardly.example

Target Market(s)

Professional Elite. Attorneys and Doctors

Industry/Entity Type

Medical Legal

Coding

Coded - Design and coding required

Number of Pages Required

5+ page

Font styles to use
Other font styles liked:
• Helvetica or maybe font that matches logo. We are open

Colors

Designer to choose colors to be used in the design.

Requirements
Must have
• I can't locate on color scale but we want Bronze and Silver/Grey from logo. Additional colors can be added. Various shades of grey
Nice to have
• Black and white photos, simple elegant design
Should not have
• Images with faces of unknown people

```html
<!DOCTYPE html>
<html lang="en">
<head>
<meta charset="utf-8">
<title>The Meridale Circle</title>
<link href="https://fonts.googleapis.com/css2?family=Arimo:wght@400;700&display=swap" rel="stylesheet">
<style>
:root{
  --bg:#f2f2f2;
  --ink:#111a24;
  --text:#2f2f2f;
  --muted:#4a4a4a;
  --bronze:#c47f52;
  --grey-btn:#878787;
  --rule:#d2d2d2;
  --white:#ffffff;
}
*{margin:0;padding:0;box-sizing:border-box}
html,body{width:1045px;height:1200px;overflow:hidden;background:var(--bg)}
body{position:relative;font-family:"Arimo",Helvetica,Arial,sans-serif;color:var(--ink)}
a{color:inherit;text-decoration:none}
.brand{position:absolute;left:29px;top:42px}
.brand-name{font-size:26px;font-weight:400;letter-spacing:-.1px;line-height:1.1}
.brand-tagline{font-size:12.5px;margin-top:14px;color:var(--ink)}
.main-nav{position:absolute;top:62px;right:29px;display:flex;gap:6px}
.nav-button{display:flex;align-items:center;justify-content:center;height:35px;padding:0 19px;font-size:11.5px;font-weight:700;color:var(--white);background:var(--grey-btn);transition:background .2s}
.nav-button:hover{background:var(--bronze)}
.nav-button.is-active{background:var(--bronze)}
.hero-image{position:absolute;left:29px;top:109px;width:987px;height:358px;
  background:radial-gradient(ellipse at 45% 55%,#f4f4f4 0%,#dcdcdc 45%,#bdbdbd 80%,#9a9a9a 100%)}
.intro{position:absolute;left:29px;top:520px;width:987px;display:flex;justify-content:space-between}
.intro-headline{width:510px;font-size:26px;font-weight:400;line-height:39px;color:var(--ink)}
.intro-text{width:430px;margin-top:37px;font-size:12.5px;line-height:22.5px;color:var(--ink)}
.newsletter{position:absolute;left:29px;top:689px;width:987px;height:67px;border-top:1px solid var(--rule);border-bottom:1px solid var(--rule);display:flex;align-items:center;justify-content:space-between}
.newsletter-label{font-size:12.5px}
.newsletter-link{font-size:11.5px;font-weight:700;color:var(--bronze);margin-right:5px}
.footer-brand{position:absolute;left:29px;top:812px;display:flex;align-items:center;gap:10px}
.footer-brand-mark{width:26px;height:26px;background:var(--bronze)}
.footer-brand-name{font-size:24px;color:#6b6b70;font-weight:400}
.footer-contact{position:absolute;left:29px;top:892px;font-size:11.5px;line-height:20.3px;color:var(--ink)}
.footer-contact strong{font-weight:700}
.footer-contact .gap{margin-top:16px}
.footer-col{position:absolute;top:806px;font-size:11.5px;line-height:23.2px;color:var(--muted)}
.footer-col h3{font-size:11.5px;font-weight:700;color:var(--ink);margin-top:12px;line-height:23.2px;margin-bottom:2px}
.footer-col h3:first-child{margin-top:0}
.footer-col a{display:block}
.footer-col a:hover{color:var(--bronze)}
.col-about{left:377px}
.col-education{left:550px}
.col-services{left:853px}
.copyright{position:absolute;left:0;width:1045px;top:1167px;text-align:center;font-size:11.5px;color:var(--muted)}
</style>
</head>
<body>
<header class="brand">
  <h1 class="brand-name">The Meridale Circle</h1>
  <p class="brand-tagline">Stewards of a fair and prompt outcome</p>
</header>
<nav class="main-nav">
  <a class="nav-button is-active" href="#">Stakeholders</a>
  <a class="nav-button" href="#">QME Physicians</a>
  <a class="nav-button" href="#">Member Physicians</a>
</nav>

<div class="hero-image" role="img" aria-label="Black and white photo of a stethoscope and pen resting on medical papers"></div>

<section class="intro">
  <h2 class="intro-headline">The Meridale Circle is a leader in Qualified Medical Evaluations and SIBTF cases in the State of California.</h2>
  <p class="intro-text">Our doctors are dedicated to facilitating settlements through rapid, objective and well researched Expert Medical Opinions.</p>
</section>

<div class="newsletter">
  <span class="newsletter-label">Most Recent Newsletter</span>
  <a class="newsletter-link" href="#">Download now</a>
</div>

<footer>
  <div class="footer-brand">
    <span class="footer-brand-mark"></span>
    <span class="footer-brand-name">Meridale Circle</span>
  </div>
  <address class="footer-contact" style="font-style:normal">
    <strong>Headquarters</strong><br>
    2780 Orchard Vale Ave.<br>
    4th Floor<br>
    Brenwick, CA 90411
    <div class="gap"><strong>Call toll free</strong> (800) 555-0148<br><strong>Fax</strong> (310) 555-0192</div>
  </address>

  <div class="footer-col col-about">
    <h3>About</h3>
    <a href="#">Company</a><a href="#">QME Locations</a><a href="#">Privacy Policy</a><a href="#">Careers</a>
    <h3>Join Us</h3>
    <a href="#">Join our network</a>
    <h3>Blog</h3>
    <a href="#">Blog</a>
  </div>
  <div class="footer-col col-education">
    <h3>Education</h3>
    <a href="#">Live Seminar QME Report Writing Course</a><a href="#">Online QME Report Writing Course</a><a href="#">QME Continuing Education (CEU)</a><a href="#">Impairment Guides 6th Edition IME Training</a>
    <h3>Contact</h3>
    <a href="#">Exam Request</a><a href="#">FAQ</a><a href="#">Locations</a><a href="#">Contact Info</a>
    <h3>Login</h3>
    <a href="#">Login To Your Account</a>
  </div>
  <div class="footer-col col-services">
    <h3>Services</h3>
    <a href="#">IME</a><a href="#">AME</a><a href="#">QME</a><a href="#">Subsequent Injuries Fund</a><a href="#">Ergonomic Evaluations</a><a href="#">Measuring Workers</a><a href="#">Pre-Employment Screenings</a><a href="#">Fit for Duty</a><a href="#">Functional Capacity Evaluation</a><a href="#">FCE &amp; Treatment Guidelines</a><a href="#">Physician’s Guide</a><a href="#">Impairment Rating</a>
  </div>
  <p class="copyright">© 2022 Clinic Jurist Panel</p>
</footer>
</body>
</html>
```